seeking a modern Business Card design for Roof Plumbering Business

wexcombe roof plumbing is a local metal re-roof and new construction specialist. We are seeking a modern business card to assist with networking within the industry. Our services are predominantly the installation of metal roofs on new houses, however we also do re-roofs when an existing roof needs replacing. We service both residential and commercial properties. Please include the below details on the card:
Name: Owen Wexcombe
Phone: 0471 385 962
Email: owenwexcomberoofing@mailnest.example

Residential & Commercial
Re-roof & New Construction
Fully Insured

I have uploaded our business logo, which we think would suit a black background. Please use all lower case for business name.
Cheers
Updates

Hey Guys, As requested I've uploaded a Pdf version of my logo. Hopefully this help. Thanks

Industry/Entity Type

Business

Contact Information for Business Card

Name: Owen Wexcombe
Phone: 0471 385 962

Residential & Commercial
Fully Insured

Font styles to use
Serif
Sans Serif

Requirements
Must have
• Name must be all lower case "wexcombe roof plumbing"
Nice to have
• Stick with Logo Colours

```html
<!DOCTYPE html>
<html lang="en">
<head>
<meta charset="utf-8">
<title>wexcombe roof plumbing — business card</title>
<link href="https://fonts.googleapis.com/css2?family=Roboto+Condensed:wght@400;700&display=swap" rel="stylesheet">
<style>
  :root {
    --page: #e4e4e2;
    --card-black: #1f1d1e;
    --brand-blue: #22a8d8;
    --band-white: #f4f6f7;
    --text-white: #ffffff;
  }
  html, body {
    margin: 0;
    width: 1200px;
    height: 800px;
    overflow: hidden;
    background: var(--page);
    font-family: "Roboto Condensed", Arial, sans-serif;
  }
  .card {
    position: absolute;
    left: 150px;
    top: 140px;
    width: 900px;
    height: 520px;
    border-radius: 34px;
    overflow: hidden;
    background: var(--card-black);
    box-shadow: 0 6px 18px rgba(0,0,0,0.18);
  }
  .card-art { position: absolute; inset: 0; }
  .contact {
    position: absolute;
    left: 52px;
    top: 218px;
    color: var(--text-white);
  }
  .contact-name {
    margin: 0 0 10px;
    font-size: 40px;
    font-weight: 700;
    letter-spacing: 0.5px;
    text-transform: uppercase;
  }
  .contact-row {
    display: flex;
    align-items: center;
    gap: 10px;
    font-size: 19px;
    line-height: 32px;
  }
  .contact-row svg { width: 22px; height: 22px; flex: none; }
  .services-band {
    position: absolute;
    left: 0;
    right: 0;
    top: 382px;
    height: 40px;
    background: var(--band-white);
    color: var(--brand-blue);
    font-size: 24px;
    line-height: 40px;
    text-align: center;
    text-transform: uppercase;
    letter-spacing: 0.3px;
    white-space: nowrap;
  }
  .brand-name {
    position: absolute;
    left: 560px;
    top: 175px;
    width: 300px;
    color: var(--brand-blue);
    font-weight: 400;
    text-align: center;
  }
  .brand-name .brand-main { display: block; font-size: 76px; line-height: 76px; }
  .brand-name .brand-sub { display: block; font-size: 30px; letter-spacing: 0.28em; margin-top: 4px; }
</style>
</head>
<body>
  <div class="card">
    <svg class="card-art" viewBox="0 0 900 520" width="900" height="520" aria-hidden="true">
      <path class="blue-panel" d="M0,0 H500 C490,220 420,400 320,520 H0 Z" fill="var(--brand-blue)"/>
      <path class="divider-line" d="M490,0 C480,220 410,400 310,520" fill="none" stroke="var(--card-black)" stroke-width="8"/>
    </svg>

    <div class="contact">
      <h1 class="contact-name">Owen Wexcombe</h1>
      <div class="contact-row">
        <svg viewBox="0 0 24 24" aria-hidden="true"><circle cx="12" cy="12" r="10" fill="none" stroke="#fff" stroke-width="1.6"/><path d="M9 7c-1 1-1.5 2-1 4 .7 2.5 2.5 4.6 4.8 5.6 1.2.5 2 .3 2.7-.5l-1.8-1.8-1.3.7c-1.2-.6-2.3-1.9-2.7-3.2l1-1.1L9 7z" fill="#fff"/></svg>
        <span>0471 385 962</span>
      </div>
      <div class="contact-row">
        <svg viewBox="0 0 24 24" aria-hidden="true"><rect x="2" y="5" width="20" height="14" fill="none" stroke="#fff" stroke-width="1.6"/><path d="M2 5l10 8 10-8M2 19l7-6M22 19l-7-6" fill="none" stroke="#fff" stroke-width="1.4"/></svg>
        <span>owenwexcomberoofing@mailnest.example</span>
      </div>
    </div>

    <div class="brand-name">
      <span class="brand-main">wexcombe</span>
      <span class="brand-sub">roof plumbing</span>
    </div>

    <div class="services-band">Residential &amp; Commercial • Re-roof &amp; New Construction • Fully Insured</div>
  </div>
</body>
</html>
```